NEW YORK Plumbing/utility company 10 year anniversary business card

Looking For simple back and front business card would like to include a few things in description
We offer 24/7 emergency service
residential
commercial
industrial
municipal
services offered
Plumbing
hydro excavation
hydro jetting
Well pumps
Sewer pumps
water mains
sewer mains

```html
<!DOCTYPE html>
<html lang="en">
<head>
<meta charset="utf-8">
<title>Ridgeline Water &amp; Sewer — Business Card</title>
<link href="https://fonts.googleapis.com/css2?family=Montserrat:wght@600;700&family=Arimo:wght@400;700&display=swap" rel="stylesheet">
<style>
  :root {
    --backdrop: #c4c4c4;
    --card-white: #ffffff;
    --brand-blue: #1e62a1;
    --deep-blue: #1b5c9e;
    --sky-blue: #2fa3e0;
    --ink: #2b2b2b;
    --white: #ffffff;
  }
  * { margin: 0; padding: 0; box-sizing: border-box; }
  html, body { width: 1200px; height: 788px; overflow: hidden; }
  body {
    background: var(--backdrop);
    display: flex;
    align-items: center;
    justify-content: center;
    gap: 40px;
    font-family: "Arimo", Arial, sans-serif;
  }
  .card {
    width: 540px;
    height: 310px;
    border-radius: 22px;
    position: relative;
    box-shadow: 0 8px 24px rgba(0,0,0,0.18);
    overflow: hidden;
  }

  /* Front */
  .card-front { background: var(--card-white); padding: 40px 40px 30px; }
  .front-top { display: flex; align-items: center; }
  .wordmark {
    font-family: "Montserrat", sans-serif;
    font-weight: 700;
    color: var(--brand-blue);
    display: flex;
    align-items: center;
    gap: 10px;
  }
  .wordmark-dot { width: 14px; height: 14px; border-radius: 50%; background: var(--brand-blue); flex: none; }
  .wordmark-name { font-size: 22px; letter-spacing: 1px; line-height: 1.1; }
  .wordmark-sub { display: block; font-size: 12px; letter-spacing: 3px; }
  .front-middle { display: flex; align-items: center; margin-top: 34px; }
  .person { width: 200px; }
  .person-name { font-weight: 700; font-size: 24px; color: var(--deep-blue); letter-spacing: 0.5px; }
  .person-title { font-size: 16px; color: var(--ink); margin-top: 4px; }
  .divider { width: 1px; height: 74px; background: var(--brand-blue); margin: 0 22px; }
  .contacts { list-style: none; font-size: 15px; color: var(--ink); line-height: 1.65; }
  .contacts li { display: flex; align-items: center; gap: 8px; }
  .contacts svg { width: 12px; height: 12px; fill: var(--sky-blue); flex: none; }
  .tagline { margin-top: 34px; font-weight: 700; font-size: 19px; color: var(--sky-blue); }
  .sectors { margin-top: 6px; font-size: 16px; color: var(--ink); }
  .sectors span::before { content: "•"; color: var(--sky-blue); margin: 0 5px 0 3px; }

  /* Back */
  .card-back {
    background: var(--brand-blue);
    color: var(--white);
    display: flex;
    flex-direction: column;
    align-items: center;
    padding: 52px 36px 30px;
  }
  .card-back .wordmark { color: var(--white); flex-direction: column; gap: 12px; text-align: center; }
  .card-back .wordmark-dot { background: var(--white); width: 18px; height: 18px; }
  .card-back .wordmark-name { font-size: 32px; letter-spacing: 3px; }
  .card-back .wordmark-sub { font-size: 15px; letter-spacing: 5px; margin-top: 6px; }
  .services-heading {
    display: flex; align-items: center; gap: 14px; width: 100%;
    margin-top: 28px;
    font-weight: 700; font-size: 20px; letter-spacing: 1px; color: var(--sky-blue);
    white-space: nowrap;
  }
  .services-heading::before, .services-heading::after { content: ""; flex: 1; height: 1.5px; background: var(--sky-blue); }
  .services { list-style: none; display: flex; flex-wrap: wrap; justify-content: center; margin-top: 12px; font-size: 16px; line-height: 1.6; max-width: 450px; }
  .services li { margin: 0 6px; }
  .services li::before { content: "•"; color: var(--sky-blue); margin-right: 4px; }
</style>
</head>
<body>
  <section class="card card-front" aria-label="Card front">
    <div class="front-top">
      <div class="wordmark">
        <span class="wordmark-dot"></span>
        <div class="wordmark-name">RIDGELINE<span class="wordmark-sub">WATER &amp; SEWER</span></div>
      </div>
    </div>
    <div class="front-middle">
      <div class="person">
        <p class="person-name">DANIEL REYES</p>
        <p class="person-title">CEO/Founder</p>
      </div>
      <div class="divider"></div>
      <ul class="contacts">
        <li><svg viewBox="0 0 24 24"><path d="M6.6 10.8a15 15 0 0 0 6.6 6.6l2.2-2.2c.3-.3.7-.4 1-.2 1.1.4 2.3.6 3.6.6.6 0 1 .4 1 1V20c0 .6-.4 1-1 1A17 17 0 0 1 3 4c0-.6.4-1 1-1h3.5c.6 0 1 .4 1 1 0 1.3.2 2.5.6 3.6.1.3 0 .7-.2 1z"/></svg>845-555-0182</li>
        <li><svg viewBox="0 0 24 24"><path d="M2 5h20v14H2z M2 5l10 8 10-8" /></svg>info@ridgelinews.com</li>
        <li><svg viewBox="0 0 24 24"><circle cx="12" cy="12" r="10"/></svg>www.ridgelinews.com</li>
      </ul>
    </div>
    <p class="tagline">We offer 24/7 emergency service</p>
    <p class="sectors"><span>Residential</span><span>Commercial</span><span>Industrial</span><span>Municipal</span></p>
  </section>

  <section class="card card-back" aria-label="Card back">
    <div class="wordmark">
      <span class="wordmark-dot"></span>
      <div class="wordmark-name">RIDGELINE<span class="wordmark-sub">WATER &amp; SEWER</span></div>
    </div>
    <h2 class="services-heading">SERVICES OFFERED</h2>
    <ul class="services">
      <li>Plumbing</li><li>Hydro excavation</li><li>Hydro jetting</li><li>Well pumps</li>
      <li>Sewer pumps</li><li>Water mains</li><li>Sewer mains</li>
    </ul>
  </section>
</body>
</html>
```